Business Card Re-design

We are looking for a fresh bold look for general office business cards. We are a staffing agency that staffs industrial, coal mining, and clerical jobs.
Tag Line: We match the BEST workers with the BEST roles.
Harlan Bay Office: 2473 W. Tallow Creek Rd, Harlan Bay, WV - 47308
p. 555.203.6180 f. 555.203.6195
Marlow Ridge Office: 264 S. Birch Ln, Marlow Ridge, WV - 47152
p. 555.319.2047 f. 555.203.6195
Absentee/Emergency 24hr Hotline 555.203.6172 opt.1
www.bluelanternworkforce.example

```html
<!DOCTYPE html>
<html lang="en">
<head>
<meta charset="utf-8">
<title>Blue Lantern Workforce — Business Card</title>
<link rel="stylesheet" href="https://fonts.googleapis.com/css2?family=Oswald:wght@500;600&family=Work+Sans:wght@400;500;600&display=swap">
<style>
  :root {
    --navy: #0b3e66;
    --green: #2f9a45;
    --band-green: #33a04a;
    --ink: #333a40;
    --paper: #ffffff;
    --backdrop: #1c1c1c;
  }
  * { box-sizing: border-box; margin: 0; padding: 0; }
  html, body { width: 1200px; height: 897px; overflow: hidden; }
  body { background: var(--backdrop); position: relative; font-family: "Work Sans", sans-serif; }

  .card {
    position: absolute;
    left: 303px;
    width: 595px;
    height: 338px;
    border-radius: 22px;
    overflow: hidden;
  }
  .card--front { top: 92px; background: var(--paper); color: var(--ink); }
  .card--back { top: 469px; background: var(--navy); }

  .holder { position: absolute; left: 32px; top: 30px; }
  .holder__name {
    font-family: "Oswald", sans-serif;
    font-weight: 600;
    font-size: 38px;
    line-height: 1;
    letter-spacing: 0.5px;
    color: var(--navy);
    text-transform: uppercase;
  }
  .holder__name .surname { color: var(--green); }
  .holder__role { font-size: 15px; letter-spacing: 0.6px; margin-top: 4px; }

  .wordmark {
    position: absolute;
    font-family: "Oswald", sans-serif;
    font-weight: 500;
    text-transform: uppercase;
    line-height: 1.02;
  }
  .wordmark--front {
    right: 31px; top: 34px;
    font-size: 30px;
    color: var(--navy);
    text-align: right;
    letter-spacing: 1px;
  }
  .wordmark--back {
    left: 0; right: 0; top: 104px;
    font-size: 46px;
    color: var(--paper);
    text-align: center;
    letter-spacing: 1.5px;
  }

  .office { position: absolute; top: 174px; font-size: 14.5px; line-height: 18.5px; letter-spacing: 0.3px; }
  .office--west { left: 32px; top: 177px; }
  .office--east { left: 386px; }
  .office__title { color: var(--green); font-weight: 600; font-size: 15.5px; margin-bottom: 1px; }
  .office__lines { margin-bottom: 4px; }
  .contact { display: flex; align-items: center; gap: 9px; height: 20px; }
  .contact svg { width: 12px; height: 12px; fill: var(--navy); flex: none; }

  .band {
    position: absolute;
    left: 0; right: 0;
    height: 26px;
    display: flex;
    align-items: center;
    color: var(--paper);
  }
  .band--front { top: 289px; background: var(--band-green); padding-left: 32px; font-size: 13.4px; letter-spacing: 0.2px; }
  .band--back { top: 288px; background: var(--band-green); justify-content: center; font-size: 17.5px; font-weight: 500; letter-spacing: 0.3px; }
  .band--back strong { font-weight: 600; }
</style>
</head>
<body>

<section class="card card--front" aria-label="Business card front">
  <div class="holder">
    <h1 class="holder__name">Daniel <span class="surname">Harper</span></h1>
    <p class="holder__role">Founder</p>
  </div>

  <div class="wordmark wordmark--front">Blue Lantern<br>Workforce</div>

  <div class="office office--west">
    <h2 class="office__title">Marlow Ridge Office:</h2>
    <p class="office__lines">264 S. Birch Ln,<br>Marlow Ridge, WV - 47152</p>
    <p class="contact"><svg viewBox="0 0 12 12" aria-label="Phone"><path d="M2.6 0.8l1.6-0.6 1.1 2.6-1 .8c.3 1.6 1.1 3 2.3 4.1l1-.7 2.3 1.6-.9 1.5C5.8 9.9 1.6 5.6 2.6 0.8z"/></svg>555.319.2047</p>
    <p class="contact"><svg viewBox="0 0 12 12" aria-label="Fax"><path d="M3 0h6v3H3zM1 3.6h10a1 1 0 0 1 1 1V9H10V7H2v2H0V4.6a1 1 0 0 1 1-1zM2.5 7.6h7V12h-7z"/></svg>555.203.6195</p>
  </div>

  <div class="office office--east">
    <h2 class="office__title">Harlan Bay Office:</h2>
    <p class="office__lines">2473 W. Tallow Creek Rd,<br>Harlan Bay, WV - 47308</p>
    <p class="contact"><svg viewBox="0 0 12 12" aria-label="Phone"><path d="M2.6 0.8l1.6-0.6 1.1 2.6-1 .8c.3 1.6 1.1 3 2.3 4.1l1-.7 2.3 1.6-.9 1.5C5.8 9.9 1.6 5.6 2.6 0.8z"/></svg>555.203.6180</p>
    <p class="contact"><svg viewBox="0 0 12 12" aria-label="Fax"><path d="M3 0h6v3H3zM1 3.6h10a1 1 0 0 1 1 1V9H10V7H2v2H0V4.6a1 1 0 0 1 1-1zM2.5 7.6h7V12h-7z"/></svg>555.203.6195</p>
  </div>

  <div class="band band--front">Emergency 24hr Hotline- 555.203.6172 or / www.bluelanternworkforce.example</div>
</section>

<section class="card card--back" aria-label="Business card back">
  <div class="wordmark wordmark--back">Blue Lantern<br>Workforce</div>
  <div class="band band--back"><p>We match the <strong>BEST</strong> workers with the <strong>BEST</strong> roles</p></div>
</section>

</body>
</html>
```